Service Plan Sales Flyer

The Watchpost Depot (www.kelvamart.com) is a commercial security integrator that installs security cameras, access control, intrusion, two-way radios and perimeter security. We require a one page flyer for our service plan for new and existing customers. The price of the service plan is $299/yr and includes the following;
1. Discounted service rate of $118/hr
2. Free remote support ($85/hr without a plan)
3. Free remote training
4. Priority support

Please review our brochure attached and create a one page sales flyer with the end goal of having the client sign up for our annual service plan . The plan will automatically renew every year. Email sales@kelvamart.com.

Target Market(s)

commercial industrial clients - no residential

Industry/Entity Type

review our website at www.kelvamart.com

Colors
0054AA
0677BA
7BADD7
CADEEF
E8F1F8
EE7325
F08F49
F5BC92
FAE3D3
FDF4ED

Requirements
Must have
• call to action
Should not have
• too many colors

```html
<!DOCTYPE html>
<html lang="en">
<head>
<meta charset="utf-8">
<title>The Watchpost Depot – Service Plan Flyer</title>
<link href="https://fonts.googleapis.com/css2?family=Montserrat:wght@400;500;600;700;800&family=Oswald:wght@600;700&display=swap" rel="stylesheet">
<style>
  :root{
    --navy:#1d2f5e;
    --orange:#ef4b36;
    --white:#ffffff;
    --ink:#2a2f3a;
    --backdrop:#8c8c8c;
    --sky-top:#8fb6da;
    --sky-bottom:#cfe2f1;
  }
  *{margin:0;padding:0;box-sizing:border-box}
  html,body{width:1200px;height:1200px;overflow:hidden;background:var(--backdrop)}
  body{font-family:'Montserrat',sans-serif;position:relative}
  .flyer{position:absolute;left:226px;top:100px;width:700px;height:990px;background:var(--white);overflow:hidden}
  .brand{position:absolute;left:49px;top:46px;width:260px;display:flex;align-items:center;gap:12px;z-index:2}
  .brand-mark{flex:none;width:26px;height:26px;background:var(--orange);border-radius:50%}
  .brand-name{font-family:'Montserrat',sans-serif;font-weight:800;font-size:20px;line-height:23px;color:var(--navy);text-transform:uppercase;letter-spacing:.3px}
  .hero-photo{position:absolute;left:328px;top:0;width:372px;height:356px;background:linear-gradient(160deg,var(--sky-top),var(--sky-bottom) 55%,#6f95bf)}
  .headline{position:absolute;left:45px;top:125px;z-index:2}
  .headline span{display:block;width:fit-content;background:var(--orange);color:var(--white);font-weight:800;font-size:36px;line-height:42px;padding:4px 22px 0 22px}
  .intro{position:absolute;left:66px;top:287px;width:250px;font-size:13px;line-height:16.2px;color:var(--ink)}
  .intro strong{color:var(--navy);font-weight:700}
  .plan-badge{position:absolute;left:404px;top:260px;width:152px;height:152px;border-radius:50%;background:var(--navy);color:var(--white);text-align:center}
  .plan-badge::before{content:"";position:absolute;inset:6px;border:1.5px dashed var(--white);border-radius:50%}
  .plan-title{font-family:'Oswald',sans-serif;font-weight:600;font-size:19px;line-height:18px;padding-top:37px}
  .plan-price{font-family:'Oswald',sans-serif;font-weight:700;font-size:46px;line-height:46px}
  .plan-price sup{color:var(--orange);font-size:30px;vertical-align:8px}
  .plan-term{font-weight:600;font-size:11px}
  .product{position:absolute;top:424px;width:180px;text-align:center}
  .product-photo{height:145px;border-radius:6px;background:linear-gradient(180deg,#eef1f5,#c9ced6)}
  .product-label{margin-top:20px;color:var(--orange);font-size:13px;font-weight:500}
  .divider{position:absolute;top:517px;height:84px;border-left:1.5px dashed var(--orange)}
  .benefits{position:absolute;left:0;top:632px;width:700px;height:233px;background:var(--navy)}
  .benefit{position:absolute;top:32px;width:150px;text-align:center;color:var(--white);font-size:15px;line-height:19px}
  .benefit-icon{width:78px;height:78px;border-radius:50%;background:var(--white);margin:0 auto 16px;display:flex;align-items:center;justify-content:center}
  .benefit .rate{color:var(--orange);font-weight:700;font-size:18px;display:block}
  .benefit small{font-size:13px;display:block}
  .accent-bar{position:absolute;left:270px;top:865px;width:160px;height:8px;background:var(--orange)}
  .cta{position:absolute;left:50px;top:906px;color:var(--navy)}
  .cta-main{font-weight:800;font-size:25px;line-height:28px}
  .cta-sub{font-weight:500;font-size:19px;line-height:24px}
  .web{position:absolute;left:386px;top:904px;display:flex;align-items:center;gap:10px}
  .web-label{font-size:17px;color:var(--navy);line-height:20px}
  .web-url{font-weight:700;font-size:22px;color:var(--orange);line-height:26px}
</style>
</head>
<body>
<div class="flyer">
  <div class="hero-photo" role="img" aria-label="Dome security camera mounted on a pole in front of a glass office tower against a blue sky"></div>

  <div class="brand"><span class="brand-mark"></span><span class="brand-name">The Watchpost<br>Depot</span></div>

  <h1 class="headline"><span>KNOWLEDGEABLE</span><span>RELIABLE</span><span>EASY</span></h1>

  <p class="intro">From it's humble beginning in 1999, The Watchpost Depot Employees have worked hard to become <strong>one of Canada's most trusted commercial security integrators.</strong></p>

  <div class="plan-badge">
    <div class="plan-title">SERVICE<br>PLAN</div>
    <div class="plan-price"><sup>$</sup>299</div>
    <div class="plan-term">PER YEAR</div>
  </div>

  <div class="product" style="left:55px">
    <div class="product-photo" role="img" aria-label="Door, monitor showing camera feed and security cameras"></div>
    <div class="product-label">Remote Access</div>
  </div>
  <div class="divider" style="left:270px"></div>
  <div class="product" style="left:288px">
    <div class="product-photo" role="img" aria-label="Keypad card reader, key fob, access card and smartphone"></div>
    <div class="product-label">Access Control</div>
  </div>
  <div class="divider" style="left:494px"></div>
  <div class="product" style="left:500px">
    <div class="product-photo" role="img" aria-label="Intrusion alarm keypad with display screen"></div>
    <div class="product-label">Intrusion Alarm</div>
  </div>

  <section class="benefits">
    <div class="benefit" style="left:31px">
      <div class="benefit-icon"><svg width="46" height="46" viewBox="0 0 46 46" fill="none" stroke="#ef4b36" stroke-width="2"><circle cx="23" cy="23" r="13"/><path d="M23 4v6M23 36v6M4 23h6M36 23h6M9.5 9.5l4 4M32.5 32.5l4 4M9.5 36.5l4-4M32.5 13.5l4-4"/><path d="M17 29l12-12"/><circle cx="18" cy="18" r="2.5"/><circle cx="28" cy="28" r="2.5"/></svg></div>
      Discounted<br>service rate of<span class="rate">$118/hr</span>
    </div>
    <div class="benefit" style="left:193px">
      <div class="benefit-icon"><svg width="48" height="46" viewBox="0 0 48 46" fill="none" stroke="#ef4b36" stroke-width="2"><rect x="4" y="4" width="11" height="11"/><rect x="18.5" y="2" width="11" height="11"/><rect x="33" y="4" width="11" height="11"/><rect x="8" y="22" width="32" height="16"/><path d="M4 42h40"/><circle cx="24" cy="28" r="3"/></svg></div>
      Free remote<br>training
    </div>
    <div class="benefit" style="left:355px">
      <div class="benefit-icon"><svg width="46" height="46" viewBox="0 0 46 46" fill="none" stroke="#ef4b36" stroke-width="2"><circle cx="26" cy="15" r="10"/><path d="M23 10v8h6"/><path d="M4 34h8l6 3h10l10-6"/><path d="M12 30h10l4 3"/></svg></div>
      Free remote<br>support<span class="rate">$85/hr</span><small>without a plan</small>
    </div>
    <div class="benefit" style="left:518px">
      <div class="benefit-icon"><svg width="50" height="46" viewBox="0 0 50 46" fill="none" stroke="#ef4b36" stroke-width="2"><path d="M3 16l9-6 8 6"/><path d="M47 16l-9-6-9 5-8 6 3 3 8-4"/><path d="M12 22l10 10a3 3 0 0 0 4-4M18 28l6 6a3 3 0 0 0 4-4M26 32a3 3 0 0 0 4-4l-6-6M38 24l-8 6"/></svg></div>
      Priority<br>support
    </div>
  </section>
  <div class="accent-bar"></div>

  <div class="cta">
    <div class="cta-main">VISIT OUR WEBSITE</div>
    <div class="cta-sub">FOR YOUR FREE QUOTE!</div>
  </div>
  <div class="web">
    <svg width="38" height="38" viewBox="0 0 38 38" fill="none" stroke="#ef4b36" stroke-width="2.2"><circle cx="19" cy="19" r="16"/><ellipse cx="19" cy="19" rx="7" ry="16"/><path d="M3 19h32M6 11h26M6 27h26"/></svg>
    <div><div class="web-label">Visit us</div><div class="web-url">www.kelvamart.com</div></div>
  </div>
</div>
</body>
</html>
```